Harbor Keyvault Password Manager WebApp Design

Harbor Keyvault is seeking an expert UI designer to provide a fresh and modern visual appeal for our product. Our inspiration comes from two major tools that have successfully managed to balance functionality and design aesthetics - Nimbus Folio and LockTrellis. We want our application to exude a similar trustworthiness and modernity, through a clean, intuitive and responsive design.
We have established preliminary mockups and would like the designer to work within these parameters while enhancing the overall user experience. The primary tasks will involve innovative and improved designs of the login screen and the password screen, both being crucial touchpoints for our users. The login screen also serves a crucial role in demonstrating how our system works.
Key Elements:
Logo Integration: We are providing the logo for Harbor Keyvault. The design should align with the logo, both in terms of colors and overall aesthetic, to ensure a cohesive brand identity.
Color Palette: The UI design should adhere to the color palette derived from the logo to maintain brand consistency. The design should effectively utilize these colors to highlight important elements and improve user engagement.
Trustworthy and Modern Design: The UI should be professional and trustworthy. It should mirror the look and feel of Nimbus Folio's simplicity and LockTrellis's solid security design, which inspires user confidence.
Adherence to Mockup Boundaries: The existing mockups serve as a guideline for the layout and placement of elements. The design should respect these boundaries while bringing innovation and visual appeal.
Improved Login Screen: The login screen is a key part of the user's journey and should be designed with utmost care. It should be intuitive, easy-to-use, visually engaging, and educative, showcasing how the system operates and encouraging users to sign in with confidence.
Enhanced Password Screen: The password screen, another key user touchpoint, needs improvement. The different types of passwords should be made more visible and intuitive, easing user interaction and enhancing the overall experience.
Prospective designers are encouraged to test our current version available for free at app.harborkeyvault.example to understand the product better and contribute to meaningful design enhancements.
The goal of this project is to provide a visually compelling and user-friendly interface for Harbor Keyvault that inspires user trust, while adhering to the branding elements, including color scheme and logo design. The ideal designer will have a proven track record of creating compelling UI designs that enhance user experience and engagement.
We preferred the design to be in Figma.
Please provide the 3 design so we can evaluate if we like to choice you:
1. Login Page.
2. Passwords View design
3. Single Passwod Page
We need all the pages to be design that are provided as screenshots.
Target Market(s)
Companies
Industry/Entity Type
Security,
Number of Pages Required
5+ page
Font styles to use
Look and feel
Each slider illustrates characteristics of the customer's brand and the style your logo design should communicate.

```html
<!DOCTYPE html>
<html lang="en">
<head>
<meta charset="utf-8">
<title>Harbor Keyvault – Login and Passwords</title>
<link href="https://fonts.googleapis.com/css2?family=Roboto:wght@300;400;500;700&display=swap" rel="stylesheet">
<style>
:root{
  --stage:#c9c9c9;
  --panel:#fbfcff;
  --panel-tint:#f4f6fb;
  --ink:#1d1d1f;
  --muted:#6b6f78;
  --line:#e3e6ec;
  --yellow:#fcd34a;
  --green:#22a45a;
  --blue:#5f89d3;
  --red:#e8553f;
  --link:#2b59c3;
  --pink:#ec3f6c;
}
*{box-sizing:border-box;margin:0;padding:0}
html,body{width:1200px;height:2552px;overflow:hidden}
body{background:var(--stage);font-family:'Roboto',sans-serif;color:var(--ink);position:relative}
.panel{position:absolute;left:98px;width:1004px;background:var(--panel);overflow:hidden}
.abs{position:absolute}
.brand-bar{position:absolute;left:0;bottom:0;width:100%;height:18px;display:flex}
.brand-bar span{flex:1}
.brand{display:flex;align-items:center;gap:12px;font-weight:300;color:#3a3d44}
.brand-square{width:36px;height:36px;background:var(--blue);border-radius:4px}
.card{background:#fff;border:1px solid var(--line);border-radius:6px;text-align:center;color:var(--muted)}
.illus{border-radius:8px}
.illus-lock{background:linear-gradient(#4a74c9,#5f89d3)}
.illus-folder{background:linear-gradient(#f2c336,#f7d24d)}
.dots{display:flex;gap:11px}
.dots i{width:10px;height:10px;border-radius:50%;background:#d4d6db}
.dots i.on{background:var(--yellow)}
.signin{background:#fff;border:1px solid var(--line);border-radius:4px;display:flex;align-items:center;padding:0 10px;gap:8px;box-shadow:0 1px 3px rgba(0,0,0,.06)}
.avatar-a{width:20px;height:20px;border-radius:50%;background:var(--pink);color:#fff;font-size:10px;display:flex;align-items:center;justify-content:center;flex:none}
.signin-text{flex:1;line-height:1.15}
.signin-text b{font-weight:500;font-size:12px;display:block}
.signin-text small{font-size:10.5px;color:var(--muted)}
.provider-dot{width:16px;height:16px;border-radius:50%;background:var(--blue);flex:none}
/* app */
.app-header{position:absolute;left:0;top:0;width:100%;height:70px;border-bottom:1px solid var(--line);background:#fff}
.search{position:absolute;left:324px;top:16px;width:432px;height:38px;border:1px solid var(--line);border-radius:3px;display:flex;align-items:center;gap:8px;padding-left:12px;font-size:11px;color:var(--muted)}
.rail{position:absolute;left:0;top:70px;width:60px;bottom:0;border-right:1px solid var(--line);background:#fff}
.rail-active{position:absolute;left:0;top:0;width:60px;height:52px;background:var(--yellow);display:flex;align-items:center;justify-content:center}
.cats{position:absolute;left:60px;top:70px;width:248px;bottom:0;border-right:1px solid var(--line);background:#fff}
.cats-head{position:absolute;left:12px;top:16px;width:224px;display:flex;justify-content:space-between;align-items:center;font-weight:500;font-size:14px}
.cat{position:absolute;left:12px;display:flex;align-items:center;gap:10px;font-size:12px;width:222px}
.cat svg{flex:none}
.cat .chev{margin-left:auto}
.cat-general{left:7px;top:57px;width:234px;height:31px;background:var(--yellow);border-radius:3px;padding-left:32px;font-size:12px}
.main-title{position:absolute;left:345px;top:89px;font-size:14px;font-weight:500}
.sort{position:absolute;left:800px;top:91px;font-size:10px;display:flex;align-items:center;gap:8px}
.tile{position:absolute;width:198px;background:#fff;border:1px solid var(--line);border-radius:4px;text-align:center;display:flex;flex-direction:column;align-items:center;justify-content:center}
.tile-name{font-size:11.5px;margin-top:4px}
.tile-mail{font-size:10px;color:var(--muted)}
.wordmark{font-size:19px;font-weight:700;color:#2b2b2b;line-height:1}
.shadowed{box-shadow:0 2px 6px rgba(0,0,0,.12)}
</style>
</head>
<body>

<!-- Login, split view -->
<section class="panel" style="top:89px;height:706px">
  <div class="abs" style="left:0;top:0;width:502px;height:100%;background:var(--panel-tint)"></div>
  <div class="brand abs" style="left:74px;top:66px;font-size:29px"><span class="brand-square"></span>Harbor Keyvault</div>

  <div class="card abs" style="left:69px;top:220px;width:192px;height:244px">
    <div class="illus illus-lock abs" role="img" aria-label="Padlock with code brackets illustration" style="left:71px;top:62px;width:52px;height:68px"></div>
    <p class="abs" style="left:28px;top:160px;width:136px;font-size:8.5px;line-height:1.3">Encrypted with different keys. The are dynamically agregated only in your store your encryption/ decryption keys.</p>
  </div>
  <div class="card abs" style="left:275px;top:220px;width:192px;height:244px;-webkit-mask-image:linear-gradient(90deg,#000 55%,transparent 85%);mask-image:linear-gradient(90deg,#000 55%,transparent 85%)">
    <div class="illus illus-folder abs" role="img" aria-label="Locked folder with password illustration" style="left:60px;top:72px;width:58px;height:58px"></div>
    <p class="abs" style="left:28px;top:165px;width:136px;font-size:8.5px;line-height:1.3">Encrypted with different keys. The are dynamically agregated only in your store your encryption decryption keys.</p>
  </div>
  <div class="dots abs" style="left:235px;top:498px"><i></i><i class="on"></i><i></i></div>

  <p class="abs" style="left:583px;top:200px;width:300px;text-align:center;font-size:17px;line-height:1.25">You can sign in or register from button below. Please keep in mind our system work</p>
  <div class="signin abs" style="left:607px;top:334px;width:248px;height:44px">
    <span class="avatar-a">A</span>
    <span class="signin-text"><b>Sign in as Avery</b><small>avery.team@harborkeyvault.example</small></span>
    <svg width="10" height="10" viewBox="0 0 10 10"><path d="M2 4l3 3 3-3" fill="none" stroke="#333" stroke-width="1.3"/></svg>
    <span class="provider-dot"></span>
  </div>

  <div class="brand-bar"><span style="background:var(--yellow)"></span><span style="background:var(--green)"></span><span style="background:var(--blue)"></span><span style="background:var(--red)"></span></div>
</section>

<!-- Login, centered view -->
<section class="panel" style="top:869px;height:761px">
  <div class="brand abs" style="left:0;width:100%;justify-content:center;top:56px;font-size:31px"><span class="brand-square" style="width:40px;height:40px"></span>Harbor Keyvault</div>
  <p class="abs" style="left:0;width:100%;top:160px;text-align:center;font-size:23px;line-height:1.28">You can sign in or register from button below.<br>Please keep in mind our system work</p>

  <div class="card abs" style="left:117px;top:259px;width:375px;height:288px">
    <div class="illus illus-lock abs" role="img" aria-label="Padlock with code brackets illustration" style="left:155px;top:74px;width:66px;height:92px"></div>
    <p class="abs" style="left:30px;top:216px;width:315px;font-size:9.5px;line-height:1.3">Encrypted with different keys. The are dynamically agregated only in your store your encryption/decryption keys.</p>
  </div>
  <div class="card abs" style="left:511px;top:259px;width:376px;height:288px">
    <div class="illus illus-folder abs" role="img" aria-label="Locked folder with password illustration" style="left:145px;top:78px;width:88px;height:92px"></div>
    <p class="abs" style="left:30px;top:214px;width:316px;font-size:9.5px;line-height:1.3">Encrypted with different keys. The are dynamically agregated only in your store your encryption/decryption keys.</p>
  </div>
  <div class="dots abs" style="left:475px;top:574px"><i></i><i class="on"></i><i></i></div>

  <div class="signin abs" style="left:378px;top:615px;width:244px;height:42px">
    <span class="avatar-a">A</span>
    <span class="signin-text"><b>Sign in as Avery</b><small>avery.team@harborkeyvault.example</small></span>
    <svg width="10" height="10" viewBox="0 0 10 10"><path d="M2 4l3 3 3-3" fill="none" stroke="#333" stroke-width="1.3"/></svg>
    <span class="provider-dot"></span>
  </div>
  <p class="abs" style="left:0;width:100%;top:678px;text-align:center;font-size:8.5px;line-height:1.35;color:var(--muted)">By clicking "continue with Orbitly" you are agree with our <a style="color:var(--link)">Terms and Use</a> learn what data<br>we collect and how we handle in it our <a style="color:var(--link)">Privacy Policy</a></p>

  <div class="brand-bar"><span style="background:var(--yellow)"></span><span style="background:var(--green)"></span><span style="background:var(--blue)"></span><span style="background:var(--red)"></span></div>
</section>

<!-- Passwords view -->
<section class="panel" style="top:1703px;height:761px;background:#fff">
  <header class="app-header">
    <div class="brand abs" style="left:24px;top:18px;font-size:19px;gap:9px"><span class="brand-square" style="width:30px;height:30px"></span>Harbor Keyvault</div>
    <div class="search"><svg width="14" height="14" viewBox="0 0 14 14"><circle cx="6" cy="6" r="4.5" fill="none" stroke="#555" stroke-width="1.3"/><path d="M9.5 9.5L13 13" stroke="#555" stroke-width="1.3"/></svg>Search</div>
    <svg class="abs" style="left:830px;top:25px" width="16" height="18" viewBox="0 0 16 18"><path d="M3 13V8a5 5 0 0110 0v5l1.5 2h-13z M6.5 16h3" fill="none" stroke="#666" stroke-width="1.2"/><circle cx="12" cy="4" r="2.5" fill="var(--red)"/></svg>
    <svg class="abs" style="left:862px;top:25px" width="18" height="18" viewBox="0 0 18 18"><circle cx="9" cy="9" r="7.5" fill="none" stroke="#666" stroke-width="1.2"/><path d="M5.5 7.5h7M5.5 10.5h5" stroke="#666" stroke-width="1.2"/></svg>
    <div class="abs" role="img" aria-label="User profile photo" style="left:896px;top:17px;width:32px;height:32px;border-radius:50%;background:linear-gradient(135deg,#5a4a45,#b9a59b)"></div>
    <svg class="abs" style="left:934px;top:30px" width="10" height="8" viewBox="0 0 10 8"><path d="M1 2l4 4 4-4" fill="none" stroke="#555" stroke-width="1.2"/></svg>
  </header>

  <nav class="rail">
    <div class="rail-active"><svg width="24" height="24" viewBox="0 0 24 24"><rect x="3" y="3" width="18" height="18" rx="2" fill="none" stroke="#333" stroke-width="1.4"/><circle cx="12" cy="12" r="4" fill="none" stroke="#333" stroke-width="1.4"/></svg></div>
    <svg class="abs" style="left:18px;top:64px" width="24" height="24" viewBox="0 0 24 24"><rect x="3" y="4" width="18" height="16" rx="2" fill="none" stroke="#444" stroke-width="1.4"/><circle cx="12" cy="12" r="3.5" fill="none" stroke="#444" stroke-width="1.4"/></svg>
    <svg class="abs" style="left:19px;top:110px" width="22" height="14" viewBox="0 0 22 14"><path d="M1 1h20M1 7h20M1 13h20" stroke="#333" stroke-width="1.6"/></svg>
  </nav>

  <aside class="cats">
    <div class="cats-head">Categories<svg width="16" height="16" viewBox="0 0 16 16"><path d="M8 1v14M1 8h14" stroke="var(--blue)" stroke-width="1.5"/></svg></div>
    <div class="abs" style="left:0;top:44px;width:100%;border-top:1px solid var(--line)"></div>
    <div class="cat cat-general">General</div>
    <div class="cat" style="top:158px"><svg width="16" height="16" viewBox="0 0 16 16"><circle cx="8" cy="8" r="6.5" fill="none" stroke="#555"/><path d="M5 8h6M8 5v6" stroke="#555"/></svg>Share with me<svg class="chev" width="12" height="8" viewBox="0 0 12 8"><path d="M1 6l5-5 5 5" fill="none" stroke="#444" stroke-width="1.3"/></svg></div>
    <div class="cat" style="top:191px;left:38px">Test 123</div>
    <div class="cat" style="top:215px;left:39px">Marketing account</div>
    <div class="cat" style="top:248px"><svg width="16" height="16" viewBox="0 0 16 16"><rect x="1.5" y="4" width="13" height="10" rx="1.5" fill="none" stroke="#555"/><path d="M5.5 4V2h5v2M1.5 8h13" stroke="#555" fill="none"/></svg>Work<svg class="chev" width="12" height="8" viewBox="0 0 12 8"><path d="M1 2l5 5 5-5" fill="none" stroke="#444" stroke-width="1.3"/></svg></div>
    <div class="cat" style="top:283px"><svg width="18" height="16" viewBox="0 0 18 16"><circle cx="5" cy="5" r="2.5" fill="none" stroke="#555"/><circle cx="13" cy="5" r="2.5" fill="none" stroke="#555"/><path d="M1 14c0-3 2-5 4-5s4 2 4 5M9 14c0-3 2-5 4-5s4 2 4 5" fill="none" stroke="#555"/></svg>Social Media</div>
    <div class="cat" style="top:318px"><svg width="16" height="16" viewBox="0 0 16 16"><path d="M3 5h10l-1 10H4z M5.5 5a2.5 2.5 0 015 0" fill="none" stroke="#555"/></svg>Shopping</div>
    <div class="cat" style="top:353px"><svg width="16" height="16" viewBox="0 0 16 16"><rect x="4" y="3" width="8" height="11" rx="1.5" fill="none" stroke="#555"/><path d="M6.5 3V1h3v2" fill="none" stroke="#555"/></svg>Travel</div>
    <div class="cat" style="top:388px"><svg width="18" height="16" viewBox="0 0 18 16"><rect x="1.5" y="3" width="15" height="11" rx="1.5" fill="none" stroke="#555"/><path d="M1.5 7h15" stroke="#555"/></svg>Banking</div>
    <div class="cat" style="top:428px"><svg width="16" height="14" viewBox="0 0 16 14"><rect x="1" y="2" width="14" height="10" fill="none" stroke="#555"/><path d="M1 2l7 6 7-6" fill="none" stroke="#555"/></svg>Emails</div>
    <div class="cat" style="top:461px"><svg width="14" height="16" viewBox="0 0 14 16"><rect x="1" y="1" width="12" height="14" rx="1" fill="none" stroke="#555"/><path d="M4 6h6M4 10h6" stroke="#555"/></svg>Import-k1 password-08.02.23</div>
    <div class="cat" style="top:494px"><svg width="14" height="16" viewBox="0 0 14 16"><rect x="1" y="1" width="12" height="14" rx="1" fill="none" stroke="#555"/><path d="M4 6h6M4 10h6" stroke="#555"/></svg>Import-k1 password-08.02.23</div>
    <div class="cat" style="top:527px"><svg width="14" height="16" viewBox="0 0 14 16"><rect x="1" y="1" width="12" height="14" rx="1" fill="none" stroke="#555"/><path d="M4 6h6M4 10h6" stroke="#555"/></svg>Import-k1 password-08.02.23</div>
    <div class="cat" style="top:567px"><svg width="18" height="14" viewBox="0 0 18 14"><path d="M1 2h5l2 2h9v9H1z" fill="none" stroke="#555"/></svg>Test</div>
    <div class="cat" style="top:600px"><svg width="18" height="16" viewBox="0 0 18 16"><rect x="1" y="2" width="16" height="12" rx="2" fill="none" stroke="#555"/><rect x="11" y="6" width="6" height="4" fill="none" stroke="#555"/></svg>Digital Wallet</div>
    <div class="cat" style="top:637px"><svg width="18" height="14" viewBox="0 0 18 14"><path d="M1 2h5l2 2h9v9H1z" fill="none" stroke="#555"/></svg>Test 215</div>
    <div class="cat" style="top:672px"><svg width="18" height="14" viewBox="0 0 18 14"><path d="M1 2h5l2 2h9v9H1z" fill="none" stroke="#555"/></svg>Test 215</div>
  </aside>

  <h2 class="main-title">All Items</h2>
  <div class="sort"><b style="font-weight:500">short by:</b> Name (a-z)
    <svg width="8" height="6" viewBox="0 0 8 6"><path d="M1 1l3 3 3-3" fill="none" stroke="#444"/></svg>
    <svg width="12" height="12" viewBox="0 0 12 12"><rect x="0" y="0" width="5" height="5" fill="var(--blue)"/><rect x="7" y="0" width="5" height="5" fill="var(--blue)"/><rect x="0" y="7" width="5" height="5" fill="var(--blue)"/><rect x="7" y="7" width="5" height="5" fill="var(--blue)"/></svg>
    <svg width="12" height="12" viewBox="0 0 12 12"><path d="M0 2h2M4 2h8M0 6h2M4 6h8M0 10h2M4 10h8" stroke="#444" stroke-width="1.4"/></svg>
  </div>

  <div class="tile shadowed" style="left:337px;top:125px;height:96px"><svg width="32" height="26" viewBox="0 0 32 26"><path d="M1.5 3h10l3 3h16v18h-29z" fill="none" stroke="#333" stroke-width="1.3"/><path d="M1.5 10h29" stroke="#333" stroke-width="1.3"/></svg><span class="tile-name">Test 123</span></div>
  <div class="tile" style="left:544px;top:125px;height:96px"><svg width="32" height="26" viewBox="0 0 32 26"><path d="M1.5 3h10l3 3h16v18h-29z" fill="none" stroke="#333" stroke-width="1.3"/><path d="M1.5 10h29" stroke="#333" stroke-width="1.3"/></svg></div>
  <div class="tile" style="left:749px;top:125px;height:96px"><svg width="32" height="26" viewBox="0 0 32 26"><path d="M1.5 3h10l3 3h16v18h-29z" fill="none" stroke="#333" stroke-width="1.3"/><path d="M1.5 10h29" stroke="#333" stroke-width="1.3"/></svg><span class="tile-name">Test 123</span></div>

  <div class="tile" style="left:337px;top:241px;height:107px"><span class="wordmark">Parcelon</span><span class="tile-name">Parcelon.example</span><span class="tile-mail">nama@mailbox.example</span></div>
  <div class="tile" style="left:544px;top:241px;height:107px"><span class="wordmark">Friendloop</span><span class="tile-name">Friendloop.example</span><span class="tile-mail">nama@mailbox.example</span></div>
  <div class="tile" style="left:749px;top:241px;height:107px"><span class="wordmark">Wikinest</span><span class="tile-name">Wikinest</span><span class="tile-mail">nama@mailbox.example</span></div>

  <div class="tile" style="left:337px;top:363px;height:107px"><span class="wordmark">Chirpline</span><span class="tile-name">Chirpline.example</span><span class="tile-mail">nama@mailbox.example</span></div>
  <div class="tile" style="left:544px;top:363px;height:107px"><svg width="30" height="30" viewBox="0 0 30 30"><circle cx="15" cy="15" r="13" fill="none" stroke="#333" stroke-width="1.3"/><ellipse cx="15" cy="15" rx="6" ry="13" fill="none" stroke="#333" stroke-width="1.3"/><path d="M2 15h26M4 8h22M4 22h22" stroke="#333" stroke-width="1.1"/></svg><span class="tile-name">Mailharbor Account</span><span class="tile-mail">nama@mailbox.example</span></div>
  <div class="tile" style="left:749px;top:363px;height:107px"><span class="wordmark">Vaultbox</span><span class="tile-name">vaultbox.example</span><span class="tile-mail">nama@mailbox.example</span></div>
</section>

</body>
</html>
```